Property inspection company needs logo/business card design

A new, home, commercial, and multi dwelling inspection company needs help with a new logo and hence business cards.

Time is extended for the rest of the week.

Font styles to use
Sans Serif

Colors
ec1f27
0255a3
ffffff

```html
<!DOCTYPE html>
<html lang="en">
<head>
<meta charset="utf-8">
<title>Rowan Hartley Property Inspections – Business Cards</title>
<link rel="stylesheet" href="https://fonts.googleapis.com/css2?family=Open+Sans:wght@400;600;700&display=swap">
<style>
  :root {
    --brand-red: #ec1f27;
    --brand-blue: #0255a3;
    --paper: #ffffff;
    --ink: #3a3a3a;
    --card-black: #141414;
    --backdrop: #2a2d31;
  }
  * { box-sizing: border-box; margin: 0; padding: 0; }
  html, body {
    width: 1200px;
    height: 900px;
    overflow: hidden;
    background: var(--backdrop);
    font-family: "Open Sans", sans-serif;
  }
  .canvas {
    position: relative;
    width: 1200px;
    height: 900px;
    display: flex;
    align-items: center;
    justify-content: center;
    gap: 60px;
  }
  .card {
    position: relative;
    width: 525px;
    height: 300px;
    border-radius: 22px;
    overflow: hidden;
  }

  /* Front */
  .card-front {
    background: var(--paper);
    color: var(--ink);
  }
  .card-front .blue-edge {
    position: absolute;
    left: 0; right: 0; bottom: 0;
    height: 14px;
    background: var(--brand-blue);
  }
  .holder {
    position: absolute;
    left: 36px;
    top: 30px;
  }
  .holder-name {
    font-size: 20px;
    font-weight: 400;
    letter-spacing: 2px;
    text-transform: uppercase;
    color: var(--ink);
  }
  .holder-title {
    margin-top: 4px;
    font-size: 11px;
    font-weight: 700;
    letter-spacing: 1px;
    color: var(--brand-red);
  }
  .rule {
    position: absolute;
    left: 36px;
    right: 36px;
    top: 96px;
    height: 1.5px;
    background: var(--brand-red);
  }
  .contacts {
    position: absolute;
    left: 36px;
    top: 116px;
    list-style: none;
    font-size: 13px;
    color: var(--ink);
  }
  .contacts li {
    display: flex;
    align-items: center;
    gap: 10px;
    margin-bottom: 10px;
  }
  .contacts svg { width: 12px; height: 12px; flex: none; }
  .front-mark {
    position: absolute;
    right: 36px;
    top: 128px;
    display: flex;
    align-items: center;
    gap: 10px;
  }
  .mark-dot {
    width: 20px;
    height: 20px;
    border-radius: 50%;
    background: var(--brand-blue);
    flex: none;
  }
  .mark-name {
    font-size: 14px;
    font-weight: 600;
    letter-spacing: 1px;
    text-transform: uppercase;
    line-height: 1.35;
    color: var(--brand-blue);
  }
  .address {
    position: absolute;
    right: 36px;
    bottom: 34px;
    font-size: 14px;
    color: var(--ink);
  }

  /* Back */
  .card-back {
    background: var(--card-black);
    display: flex;
    align-items: center;
    justify-content: center;
  }
  .card-back .mark-dot { width: 26px; height: 26px; }
  .card-back .mark-name {
    font-size: 20px;
    color: var(--paper);
  }
  .back-mark {
    display: flex;
    align-items: center;
    gap: 14px;
  }
</style>
</head>
<body>
<main class="canvas">

  <section class="card card-front" aria-label="Business card front">
    <div class="holder">
      <h1 class="holder-name">Rowan Hartley</h1>
      <p class="holder-title">JOB TITLE</p>
    </div>
    <div class="rule"></div>
    <ul class="contacts">
      <li>
        <svg viewBox="0 0 12 12" aria-hidden="true"><rect x="3" y="0.5" width="6" height="11" rx="1.2" fill="#ec1f27"/><rect x="4" y="2" width="4" height="7" fill="#fff"/></svg>
        000 000 0000
      </li>
      <li>
        <svg viewBox="0 0 12 12" aria-hidden="true"><rect x="0.5" y="2" width="11" height="8" rx="1" fill="#ec1f27"/><path d="M1 2.6 L6 6.8 L11 2.6" fill="none" stroke="#fff" stroke-width="1"/></svg>
        youremail@xyz.com
      </li>
      <li>
        <svg viewBox="0 0 12 12" aria-hidden="true"><circle cx="6" cy="6" r="5.5" fill="#ec1f27"/><path d="M0.5 6 H11.5 M6 0.5 V11.5" stroke="#fff" stroke-width="0.8"/><ellipse cx="6" cy="6" rx="2.4" ry="5.5" fill="none" stroke="#fff" stroke-width="0.8"/></svg>
        www.yourwebsite.com
      </li>
    </ul>
    <div class="front-mark">
      <span class="mark-dot"></span>
      <span class="mark-name">Rowan Hartley<br>Property Inspections Inc.</span>
    </div>
    <p class="address">Your Address here</p>
    <div class="blue-edge"></div>
  </section>

  <section class="card card-back" aria-label="Business card back">
    <div class="back-mark">
      <span class="mark-dot"></span>
      <span class="mark-name">Rowan Hartley<br>Property Inspections Inc.</span>
    </div>
  </section>

</main>
</body>
</html>
```